logo & Business Card Design

NovaGuard Termite & Pest Control, I need a great logo, take my ideas and run with them!
I will use this in marketing and website so needs to be eye catching but professional

Target Market(s)

Resedintial & Business

Industry/Entity Type

Marketing

Contact Information for Business Card

Need front side with pertinent info & Logo; back side will have a 25% off initial services Coupon!

Font styles to use
Sans Serif

Colors
ec1f27
1b1b1b

Requirements
Must have
• Professional logo and style
Nice to have
• Raised lettering, black, red, white colors maybe? I'm flexible, but those colors go good on any background, vehicle, uniform, etc...
Should not have
• Cheesy

```html
<!DOCTYPE html>
<html lang="en">
<head>
<meta charset="utf-8">
<title>NovaGuard Termite &amp; Pest Control – Logo &amp; Business Card</title>
<link rel="stylesheet" href="https://fonts.googleapis.com/css2?family=Oswald:wght@500;700&family=Roboto:wght@400;500&display=swap">
<style>
  :root {
    --stage-top: #e4e4e4;
    --stage-bottom: #ffffff;
    --card-top: #fbfaf0;
    --card-mid: #e9e8dc;
    --card-bottom: #44442e;
    --brand-orange: #e88a12;
    --brand-gold: #c99a2a;
    --ink: #1b1b1b;
    --ink-soft: #3a3a32;
    --on-dark: #f3f1e4;
    --mark-fill: #e07b10;
  }
  * { box-sizing: border-box; margin: 0; padding: 0; }
  html, body { width: 1200px; height: 450px; overflow: hidden; }
  body {
    position: relative;
    background: linear-gradient(180deg, var(--stage-top) 0%, var(--stage-bottom) 70%);
    font-family: "Roboto", Arial, sans-serif;
  }

  /* Business card front */
  .card {
    position: absolute;
    left: 60px; top: 60px;
    width: 537px; height: 327px;
    background: linear-gradient(180deg, var(--card-top) 0%, var(--card-mid) 45%, #b9b8a4 68%, var(--card-bottom) 100%);
    box-shadow: 4px 8px 14px rgba(0,0,0,.35);
  }
  .card-brand {
    position: absolute;
    left: 54px; top: 58px;
    width: 150px;
    text-align: center;
    font-family: "Oswald", "Arial Narrow", sans-serif;
    font-weight: 700;
    color: var(--brand-orange);
    text-transform: uppercase;
    line-height: 1.1;
  }
  .card-brand .brand-name { display: block; font-size: 22px; letter-spacing: .5px; }
  .card-brand .brand-line { display: block; font-size: 11px; letter-spacing: .3px; }
  .card-brand-dot {
    position: absolute;
    left: 89px; top: 118px;
    width: 80px; height: 80px;
    border-radius: 50%;
    background: var(--mark-fill);
  }
  .contact {
    position: absolute;
    right: 42px; top: 112px;
    text-align: right;
    color: var(--ink);
  }
  .contact .person-name { font-size: 22px; font-weight: 400; letter-spacing: .5px; line-height: 1.1; }
  .contact .person-role { font-size: 15px; color: var(--brand-gold); letter-spacing: .5px; margin-top: 2px; }
  .contact-lines {
    position: absolute;
    right: 82px; top: 173px;
    text-align: right;
    color: var(--on-dark);
    font-size: 12px;
    letter-spacing: .4px;
  }
  .contact-lines .phone { font-size: 16px; margin-bottom: 16px; color: #f6f4e6; }
  .contact-lines .email, .contact-lines .web { line-height: 19px; }
  .contact-icon {
    position: absolute;
    right: 64px;
    width: 17px; height: 17px;
  }
  .contact-icon.phone-icon { top: 177px; }
  .contact-icon.mail-icon { top: 209px; }
  .tagline {
    position: absolute;
    left: 0; right: 0; top: 267px;
    text-align: center;
    font-family: "Oswald", "Arial Narrow", sans-serif;
    font-weight: 500;
    font-style: italic;
    font-size: 16px;
    letter-spacing: 1.2px;
    color: var(--brand-orange);
    text-transform: uppercase;
  }

  /* Standalone logo lockup */
  .logo-lockup {
    position: absolute;
    left: 770px; top: 52px;
    width: 275px;
    text-align: center;
    font-family: "Oswald", "Arial Narrow", sans-serif;
    font-weight: 700;
    color: var(--brand-orange);
    text-transform: uppercase;
    line-height: 1.05;
  }
  .logo-lockup .brand-name { display: block; font-size: 46px; letter-spacing: 1px; }
  .logo-lockup .brand-line { display: block; font-size: 21px; letter-spacing: .5px; }
  .logo-lockup-dot {
    position: absolute;
    left: 832px; top: 170px;
    width: 150px; height: 150px;
    border-radius: 50%;
    background: var(--mark-fill);
  }
</style>
</head>
<body>
  <section class="card" aria-label="Business card front">
    <div class="card-brand">
      <span class="brand-name">NovaGuard</span>
      <span class="brand-line">Termite &amp; Pest Control</span>
    </div>
    <div class="card-brand-dot"></div>

    <div class="contact">
      <p class="person-name">DANIEL BROOKS</p>
      <p class="person-role">PRESIDENT</p>
    </div>

    <div class="contact-lines">
      <p class="phone">555-014-2290</p>
      <p class="email">DAN@NOVAGUARDPEST.COM</p>
      <p class="web">WWW.NOVAGUARDPESTCONTROL.COM</p>
    </div>

    <svg class="contact-icon phone-icon" viewBox="0 0 20 20" aria-hidden="true">
      <circle cx="10" cy="10" r="9" fill="none" stroke="#d9b24a" stroke-width="1.5"/>
      <path d="M7 5.5l2 2-1 1.3c.6 1.3 1.6 2.3 2.9 2.9l1.3-1 2 2-1.2 1.5c-3.6-.4-6.5-3.3-6.9-6.9z" fill="#d9b24a"/>
    </svg>
    <svg class="contact-icon mail-icon" viewBox="0 0 20 20" aria-hidden="true">
      <circle cx="10" cy="10" r="9" fill="none" stroke="#d9b24a" stroke-width="1.5"/>
      <rect x="5.5" y="7" width="9" height="6.5" fill="none" stroke="#d9b24a" stroke-width="1.2"/>
      <path d="M5.5 7l4.5 3.5L14.5 7" fill="none" stroke="#d9b24a" stroke-width="1.2"/>
    </svg>

    <p class="tagline">A shield of protection for your home or business</p>
  </section>

  <section class="logo-lockup" aria-label="Logo">
    <span class="brand-name">NovaGuard</span>
    <span class="brand-line">Termite &amp; Pest Control</span>
  </section>
  <div class="logo-lockup-dot"></div>
</body>
</html>
```